Business Card Design Project

Im an electrician and my company name is Kestrel Electrical
My main work is installing Lighting and Power Points, Home Theater Systems, TVS, Phones and Data
Im looking a business card, something nice, clean, modern and not to cluttered
Im open to sugestions
I dont mind if the "Services" is on the back on the business card
colours black, grey, white or the blue colour of my logo are prefered but not compulsory
any questions just message me
and please make it so if i need to edit the writing can do it easy. maybe by making it a seperate layer ?
My Details are.
Name - Peter Halloran
Job Title - Licenced Electrician
Mobile - 027 583 2174
Email - peter@kestrelelectrical.co.nz
Web - www.kestrelelectrical.co.nz
Services
Residential / Commercial
Lighting & Power
Heating & Ventilation
Automation
Phone & Data
Home Cinema
Sound Systems
TV, Antenna & Satellite
Digital Upgrades

```html
<!DOCTYPE html>
<html lang="en">
<head>
<meta charset="utf-8">
<title>Kestrel Electrical – Business Card</title>
<link href="https://fonts.googleapis.com/css2?family=Lato:wght@400;700&display=swap" rel="stylesheet">
<style>
  :root {
    --ink: #1b1b1b;
    --paper: #ffffff;
    --brand-blue: #11a3c3;
    --text: #222222;
    --backdrop: #eceff1;
  }
  * { margin: 0; padding: 0; box-sizing: border-box; }
  html, body {
    width: 1200px; height: 602px; overflow: hidden;
    background: var(--backdrop);
    font-family: "Lato", "Helvetica Neue", Arial, sans-serif;
  }
  .canvas { position: relative; width: 1200px; height: 602px; }
  .card-art { position: absolute; inset: 0; }
  .front-content { position: absolute; left: 657px; top: 180px; color: var(--text); }
  .wordmark {
    display: flex; flex-direction: column;
    font-weight: 700; color: var(--brand-blue);
    font-size: 27px; letter-spacing: 1.5px; line-height: 1.08;
    text-transform: uppercase;
  }
  .wordmark .line2 { padding-left: 70px; }
  .holder { margin-top: 48px; }
  .holder-name {
    font-weight: 700; font-size: 18px; letter-spacing: 1.5px;
    font-variant: small-caps; color: var(--ink);
  }
  .holder-title { font-size: 14px; margin-top: 3px; }
  .contact-list { list-style: none; margin-top: 26px; }
  .contact-list li {
    display: flex; align-items: center; gap: 8px;
    font-size: 16px; height: 21px; margin-bottom: 10px;
  }
  .contact-icon { width: 21px; height: 21px; flex: none; }
</style>
</head>
<body>
<main class="canvas">
  <svg class="card-art" width="1200" height="602" viewBox="0 0 1200 602" aria-hidden="true">
    <!-- back of card -->
    <polygon class="back-accent" points="165,150 40,483 170,483" fill="var(--brand-blue)"/>
    <rect class="card-back" x="165" y="148" width="415" height="337" fill="var(--ink)"/>
    <!-- front of card -->
    <rect class="card-front" x="622" y="148" width="523" height="337" fill="var(--paper)"/>
    <polygon class="front-accent" points="1036,148 1168,485 1040,485" fill="var(--brand-blue)"/>
    <rect class="front-band" x="622" y="462" width="418" height="23" fill="var(--ink)"/>
  </svg>

  <section class="front-content">
    <div class="wordmark">
      <span class="line1">Kestrel</span>
      <span class="line2">Electrical</span>
    </div>
    <div class="holder">
      <p class="holder-name">Peter Halloran</p>
      <p class="holder-title">Licenced Electrician</p>
    </div>
    <ul class="contact-list">
      <li>
        <svg class="contact-icon" viewBox="0 0 21 21" aria-hidden="true">
          <rect width="21" height="21" rx="4" fill="var(--ink)"/>
          <path d="M6.5 4.5 L8.5 4.5 L9.5 7.5 L8 8.8 Q9.5 11.8 12.2 13 L13.5 11.5 L16.5 12.5 L16.5 14.5 Q15.5 16.5 13 16 Q6 13.5 5 7 Q5 5 6.5 4.5 Z" fill="var(--paper)"/>
        </svg>
        <span>027 583 2174</span>
      </li>
      <li>
        <svg class="contact-icon" viewBox="0 0 21 21" aria-hidden="true">
          <rect width="21" height="21" rx="4" fill="var(--ink)"/>
          <rect x="4.5" y="6" width="12" height="9" fill="none" stroke="var(--paper)" stroke-width="1.5"/>
          <path d="M4.5 6 L10.5 11 L16.5 6" fill="none" stroke="var(--paper)" stroke-width="1.5"/>
        </svg>
        <span>peter@kestrelelectrical.co.nz</span>
      </li>
      <li>
        <svg class="contact-icon" viewBox="0 0 21 21" aria-hidden="true">
          <rect width="21" height="21" rx="4" fill="var(--ink)"/>
          <g fill="none" stroke="var(--paper)" stroke-width="1.2">
            <circle cx="10.5" cy="10.5" r="6"/>
            <ellipse cx="10.5" cy="10.5" rx="2.6" ry="6"/>
            <line x1="4.5" y1="10.5" x2="16.5" y2="10.5"/>
            <line x1="5.5" y1="7.5" x2="15.5" y2="7.5"/>
            <line x1="5.5" y1="13.5" x2="15.5" y2="13.5"/>
          </g>
        </svg>
        <span>www.kestrelelectrical.co.nz</span>
      </li>
    </ul>
  </section>
</main>
</body>
</html>
```